Business Card Design

The new Company is called The Harbor Pantry - based in Miami Beach, Florida and Connecticut. We want a business card to be catchy and memorable ( like our Company name). Our business is marketing and retail sales of flavored cashew nuts in boutique /high end stores. The new business card must include a logo which must be a cashew nut with a king's crown or Roman wreath.
Yes- we are looking for a logo to be designed for the business and for the business card.

Industry/Entity Type

Marketing

Font styles to use
Script

```html
<!DOCTYPE html>
<html lang="en">
<head>
<meta charset="utf-8">
<title>The Harbor Pantry – Business Card</title>
<link rel="stylesheet" href="https://fonts.googleapis.com/css2?family=Montserrat:wght@600&family=Questrial&display=swap">
<style>
  :root {
    --stage-center: #2c2c2c;
    --stage-edge: #050505;
    --card-light: #ad1229;
    --card-mid: #8d0a19;
    --card-dark: #6a0009;
    --gold: #d8a860;
    --gold-deep: #b9803b;
    --ink: #ffffff;
  }
  * { box-sizing: border-box; margin: 0; padding: 0; }
  html, body { width: 1200px; height: 761px; overflow: hidden; }
  body {
    position: relative;
    background: radial-gradient(ellipse 560px 460px at 600px 360px, var(--stage-center) 0%, #1a1a1a 55%, var(--stage-edge) 100%);
    font-family: "Questrial", "Century Gothic", sans-serif;
    color: var(--ink);
  }
  .card {
    position: absolute;
    left: 451px; top: 118px;
    width: 298px; height: 495px;
    background: radial-gradient(ellipse 220px 300px at 150px 210px, var(--card-light) 0%, var(--card-mid) 50%, var(--card-dark) 100%);
    overflow: hidden;
  }
  .card-swoosh { position: absolute; left: 0; top: 0; }
  .brand-mark {
    position: absolute;
    left: 114px; top: 58px;
    width: 70px; height: 70px;
    border-radius: 50%;
    background: var(--gold);
  }
  .brand-name {
    position: absolute;
    left: 0; top: 158px; width: 298px;
    text-align: center;
    font-size: 22px;
    letter-spacing: 0.5px;
    color: var(--ink);
  }
  .holder {
    position: absolute;
    right: 42px; top: 264px;
    text-align: right;
  }
  .holder-name {
    font-family: "Montserrat", "Century Gothic", sans-serif;
    font-weight: 600;
    font-size: 23px;
    line-height: 26px;
  }
  .holder-role {
    font-size: 16px;
    line-height: 18px;
  }
  .contact {
    position: absolute;
    display: flex;
    align-items: center;
    font-size: 13px;
    line-height: 16px;
  }
  .contact svg { flex: none; fill: var(--ink); }
  .contact--phone { left: 73px; top: 324px; }
  .contact--phone svg { margin-right: 12px; }
  .contact--mail { left: 52px; top: 355px; }
  .contact--mail svg { margin-right: 11px; }
  .contact--web { left: 44px; top: 385px; }
  .contact--web svg { margin-right: 9px; }
  .contact--place { left: 41px; top: 419px; align-items: flex-start; }
  .contact--place svg { margin-right: 16px; margin-top: 2px; }
</style>
</head>
<body>
  <main class="card">
    <svg class="card-swoosh" width="298" height="495" viewBox="0 0 298 495" aria-hidden="true">
      <path d="M276 168 C262 215 190 232 130 280 C70 328 28 395 30 476 C38 400 80 335 138 287 C196 240 270 218 276 168 Z" fill="var(--gold)"/>
    </svg>

    <div class="brand-mark" aria-hidden="true"></div>
    <p class="brand-name">The Harbor Pantry</p>

    <div class="holder">
      <p class="holder-name">Alex Moreno</p>
      <p class="holder-role">General Manager</p>
    </div>

    <p class="contact contact--phone">
      <svg width="16" height="16" viewBox="0 0 24 24" aria-hidden="true"><path d="M6.6 10.8a15.1 15.1 0 0 0 6.6 6.6l2.2-2.2a1 1 0 0 1 1-.25 11.4 11.4 0 0 0 3.6.57 1 1 0 0 1 1 1V20a1 1 0 0 1-1 1A17 17 0 0 1 3 4a1 1 0 0 1 1-1h3.5a1 1 0 0 1 1 1c0 1.25.2 2.45.57 3.57a1 1 0 0 1-.25 1z"/></svg>
      +1 305 555 01 42
    </p>
    <p class="contact contact--mail">
      <svg width="19" height="13" viewBox="0 0 19 13" aria-hidden="true"><path d="M0 0h19v13H0z"/><path d="M1 1l8.5 6.5L18 1" fill="none" stroke="#8d0a19" stroke-width="1.4"/></svg>
      alex@theharborpantry.com
    </p>
    <p class="contact contact--web">
      <svg width="23" height="23" viewBox="0 0 23 23" aria-hidden="true"><circle cx="11.5" cy="11.5" r="11.5"/><rect x="2" y="9" width="19" height="5" fill="#8d0a19"/><path d="M11.5 2v19M4 5.5h15M4 17.5h15" stroke="#8d0a19" stroke-width="1.2" fill="none"/></svg>
      www.theharborpantry.com
    </p>
    <p class="contact contact--place">
      <svg width="21" height="28" viewBox="0 0 21 28" aria-hidden="true"><path d="M10.5 0A10.5 10.5 0 0 0 0 10.5C0 18 10.5 28 10.5 28S21 18 21 10.5A10.5 10.5 0 0 0 10.5 0zm0 14.5a4 4 0 1 1 0-8 4 4 0 0 1 0 8z"/></svg>
      <span>48 Bayview Lantern road<br>miami beach, FL 33139</span>
    </p>
  </main>
</body>
</html>
```